Realtor needs 8 1/2 x 11 flyer designed both sides

I uploaded a new word doc to be used under each of the pictures on the front page.

Colors

Designer to choose colors to be used in the design.

```html
<!DOCTYPE html>
<html lang="en">
<head>
<meta charset="utf-8">
<title>Realtor Flyer – Front and Back</title>
<link rel="stylesheet" href="https://fonts.googleapis.com/css2?family=Open+Sans:wght@300;400;600&family=Tinos:wght@400;700&display=swap">
<style>
  :root {
    --backdrop: #e4e4e4;
    --panel-grey: #f1f1f1;
    --white: #ffffff;
    --blue: #3a62ad;
    --navy: #23418a;
    --accent-blue: #2f5bb0;
    --ink: #2b2b2b;
    --muted: #5a5a5a;
    --sans: 'Open Sans', Arial, sans-serif;
    --serif: 'Tinos', 'Times New Roman', serif;
  }
  * { box-sizing: border-box; margin: 0; padding: 0; }
  html, body { width: 1200px; height: 818px; overflow: hidden; }
  body { background: var(--backdrop); position: relative; font-family: var(--sans); color: var(--ink); }

  .page {
    position: absolute; top: 85px; width: 500px; height: 647px;
    background: var(--panel-grey); overflow: hidden;
    box-shadow: 0 3px 10px rgba(0,0,0,.25);
  }
  .page--inside { left: 72px; }
  .page--cover { left: 628px; }
  .page > * { position: absolute; }
  .shapes { left: 0; top: 0; width: 500px; height: 647px; }

  /* inside page */
  .hero-title {
    left: 15px; top: 30px; font-family: var(--serif); font-weight: 700;
    font-size: 37px; line-height: 37px; color: var(--white); letter-spacing: .5px;
    text-shadow: 0 1px 3px rgba(0,0,0,.4);
  }
  .headshot { width: 76px; height: 76px; top: 226px; border: 1px solid #d0d0d0; }
  .headshot--laura { left: 14px; background: linear-gradient(160deg, #e7d3b0, #c9a679 55%, #3a3a3a); }
  .headshot--marion { left: 259px; background: linear-gradient(160deg, #f4ede3, #e2c9a4 55%, #2c2c2c); }
  .agent-id { top: 255px; font-size: 8.5px; line-height: 12px; color: var(--muted); }
  .agent-id small { font-size: 6px; display: block; line-height: 9px; }
  .agent-id--laura { left: 99px; }
  .agent-id--marion { left: 344px; }
  .note-heading { top: 291px; font-size: 13px; font-weight: 400; color: var(--accent-blue); letter-spacing: .1px; }
  .note-heading--laura { left: 99px; }
  .note-heading--marion { left: 344px; }
  .note-body { top: 314px; width: 227px; font-size: 6.9px; line-height: 8.9px; text-align: justify; letter-spacing: -.15px; color: var(--ink); }
  .note-body p { margin-bottom: 9px; }
  .note-body--laura { left: 14px; }
  .note-body--marion { left: 259px; }

  .footer-name { top: 580px; font-size: 11.5px; font-weight: 600; color: var(--white); letter-spacing: .2px; }
  .contact-list { top: 602px; list-style: none; font-size: 8px; line-height: 14px; color: var(--white); }
  .contact-list li { display: flex; align-items: center; gap: 6px; }
  .contact-list svg { width: 10px; height: 10px; flex: none; }
  .footer-name--left, .contact-list--left { left: 14px; }
  .footer-name--right, .contact-list--right { right: 14px; text-align: right; }
  .contact-list--right li { justify-content: flex-end; }

  /* cover page */
  .brand { left: 20px; top: 38px; display: flex; align-items: center; gap: 8px; }
  .brand-square { width: 14px; height: 14px; background: #a9a9a9; }
  .brand-name { font-family: var(--serif); font-size: 26px; font-weight: 400; color: var(--accent-blue); }
  .postage {
    left: 452px; top: 22px; width: 33px; height: 33px; border: 1px solid #333;
    font-size: 3.6px; line-height: 4.4px; font-weight: 600; text-align: center; padding-top: 3px; color: #222;
  }
  .mail-to { left: 400px; top: 60px; font-size: 7px; line-height: 9px; font-weight: 600; color: #222; }
  .portrait {
    left: 18px; top: 348px; width: 175px; height: 235px; border-radius: 80px 80px 0 0;
    background: linear-gradient(180deg, #e4cc9f 0%, #c9a36e 40%, #2a2a2a 85%);
  }
  .cover-id { left: 196px; top: 449px; font-size: 12px; line-height: 17px; color: var(--muted); }
  .cover-id small { display: block; font-size: 8px; line-height: 14px; }
  .cover-message { left: 196px; top: 503px; font-family: var(--serif); font-size: 12.5px; line-height: 15px; color: #222; }
  .partner { left: 398px; top: 462px; display: flex; flex-direction: column; align-items: center; gap: 6px; width: 84px; }
  .partner-circle { width: 40px; height: 40px; border-radius: 50%; background: var(--navy); }
  .partner-name { font-size: 11px; font-weight: 600; color: var(--navy); text-align: center; line-height: 13px; }
  .badge { top: 598px; width: 24px; height: 24px; background: #9fb1d6; }
  .badge--one { left: 418px; }
  .badge--two { left: 452px; }
</style>
</head>
<body>

<!-- Inside page -->
<section class="page page--inside">
  <svg class="shapes" viewBox="0 0 500 647">
    <defs>
      <linearGradient id="resortTone" x1="0" y1="0" x2="1" y2="1">
        <stop offset="0" stop-color="#3b3f63"/>
        <stop offset=".55" stop-color="#6a5a55"/>
        <stop offset="1" stop-color="#1c2136"/>
      </linearGradient>
    </defs>
    <polygon role="img" aria-label="Evening photograph of a modern home with a lit lounge and pool" points="0,0 500,0 500,123 0,160" fill="url(#resortTone)"/>
    <polygon points="352,196 500,123 500,250" fill="var(--navy)"/>
    <polygon points="500,540 164,609 164,647 500,647" fill="var(--navy)"/>
    <polygon points="0,530 311,591 245,647 0,647" fill="var(--blue)"/>
  </svg>

  <h1 class="hero-title">WHY<br>CHOSE US?</h1>

  <div class="headshot headshot--laura" role="img" aria-label="Headshot of Laura Bellamy"></div>
  <div class="agent-id agent-id--laura">Laura Bellamy<br>Realtor ®<small>DRE# 02281745</small></div>
  <h2 class="note-heading note-heading--laura">A NOTE FROM LAURA</h2>

  <div class="headshot headshot--marion" role="img" aria-label="Headshot of Marion Stead"></div>
  <div class="agent-id agent-id--marion">Marion Stead<br>Realtor ®<small>DRE# 00714392</small></div>
  <h2 class="note-heading note-heading--marion">A NOTE FROM MARION</h2>

  <div class="note-body note-body--laura">
    <p>I know many of you, but for those whom I do not, I'd like to introduce myself. I've been a resident of Harbor Crest for almost 23 years now. I've loved our neighborhood from the first time I discovered it. From our beautiful parks to our fabulous pool and amenities, it's hard to beat our wonderful community.</p>
    <p>I always say where we live is the next best thing to living on a tropical island. I've traveled to many and I'm always happy to come back to my Harbor Crest home. My passion for this area is why I'm in Real Estate. I consider myself incredibly fortunate to sell homes and help people purchase homes in an area that I love with all my heart.</p>
    <p>Marion and I have been close colleagues for the last 8 years, both working as Realtors and long time residents of Harbor Crest. I am most grateful for our working relationship and the friendship we have formed. I am humbled by her trust and respect for me.</p>
    <p>Please feel welcome to call on me for all things home-related. I will look forward to meeting you!</p>
  </div>

  <div class="note-body note-body--marion">
    <p>I have exciting and bittersweet news I want to share with my Harbor Crest clients, friends and neighbors. After 40 (something) years in the Real Estate business, I have decided to retire. Some of you may know last month I sold my Harbor Crest home and moved to the beautiful Oakmere Glen community in Valle Sereno.</p>
    <p>My husband and I wanted to scale down and have time to enjoy retirement, together. I have been so blessed to have had an illustrious career in Real Estate and I want to thank you with a most grateful heart for giving me the opportunity to work with you. I have enjoyed every minute. I'm happy and proud to be turning my business over to Laura Bellamy, fellow Summit Realty agent. She and I have enjoyed a very close working relationship for many years and there is nobody else except Laura I'd consider turning my business over to. Laura is....I will add verbiage here conveying your thoughts about me. Please contact me if you'd like a personal introduction to Laura or contact her directly.</p>
    <p>Remember to mention me when you contact Laura and let her know that we know each other. I wish you the very best and please say hello when you see me in the neighborhood.</p>
  </div>

  <h3 class="footer-name footer-name--left">LAURA BELLAMY</h3>
  <ul class="contact-list contact-list--left">
    <li><svg viewBox="0 0 10 10"><circle cx="5" cy="5" r="4.4" fill="none" stroke="#fff" stroke-width=".8"/><path d="M3.3 2.8l1 1-.5.6a4 4 0 0 0 1.8 1.8l.6-.5 1 1-.7.8C4.6 7.2 2.8 5.4 2.5 3.5z" fill="#fff"/></svg>555 014 2283</li>
    <li><svg viewBox="0 0 10 10"><circle cx="5" cy="5" r="4.4" fill="none" stroke="#fff" stroke-width=".8"/><rect x="2.6" y="3.3" width="4.8" height="3.4" fill="none" stroke="#fff" stroke-width=".7"/><path d="M2.6 3.3L5 5.2l2.4-1.9" fill="none" stroke="#fff" stroke-width=".7"/></svg>laura@bellamyhomes.com</li>
    <li><svg viewBox="0 0 10 10"><circle cx="5" cy="5" r="4.4" fill="none" stroke="#fff" stroke-width=".8"/><circle cx="5" cy="5" r="2.6" fill="none" stroke="#fff" stroke-width=".6"/><path d="M2.4 5h5.2M5 2.4v5.2" stroke="#fff" stroke-width=".6"/></svg>www.bellamyhomes.com</li>
  </ul>

  <h3 class="footer-name footer-name--right">MARION STEAD</h3>
  <ul class="contact-list contact-list--right">
    <li>555 019 4471<svg viewBox="0 0 10 10"><circle cx="5" cy="5" r="4.4" fill="none" stroke="#fff" stroke-width=".8"/><path d="M3.3 2.8l1 1-.5.6a4 4 0 0 0 1.8 1.8l.6-.5 1 1-.7.8C4.6 7.2 2.8 5.4 2.5 3.5z" fill="#fff"/></svg></li>
    <li>marion@marionstead.com<svg viewBox="0 0 10 10"><circle cx="5" cy="5" r="4.4" fill="none" stroke="#fff" stroke-width=".8"/><rect x="2.6" y="3.3" width="4.8" height="3.4" fill="none" stroke="#fff" stroke-width=".7"/><path d="M2.6 3.3L5 5.2l2.4-1.9" fill="none" stroke="#fff" stroke-width=".7"/></svg></li>
    <li>www.marionstead.com<svg viewBox="0 0 10 10"><circle cx="5" cy="5" r="4.4" fill="none" stroke="#fff" stroke-width=".8"/><circle cx="5" cy="5" r="2.6" fill="none" stroke="#fff" stroke-width=".6"/><path d="M2.4 5h5.2M5 2.4v5.2" stroke="#fff" stroke-width=".6"/></svg></li>
  </ul>
</section>

<!-- Cover page -->
<section class="page page--cover">
  <svg class="shapes" viewBox="0 0 500 647">
    <defs>
      <linearGradient id="communityTone" x1="0" y1="0" x2="0" y2="1">
        <stop offset="0" stop-color="#9cc0e6"/>
        <stop offset=".45" stop-color="#5f8a4c"/>
        <stop offset="1" stop-color="#6f8f7e"/>
      </linearGradient>
    </defs>
    <rect x="0" y="0" width="500" height="130" fill="var(--white)"/>
    <polygon role="img" aria-label="Photograph of the community entrance sign with fountains and palm trees" points="0,124 500,124 500,356 0,405" fill="url(#communityTone)"/>
    <polygon points="269,160 500,91 500,140" fill="var(--navy)"/>
    <polygon points="500,540 164,609 164,647 500,647" fill="var(--navy)"/>
    <polygon points="0,530 311,591 245,647 0,647" fill="var(--blue)"/>
  </svg>

  <div class="brand">
    <span class="brand-square"></span>
    <span class="brand-name">Laura Bellamy</span>
  </div>

  <div class="postage">PRSRT STD<br>ECRWSS<br>U.S. POSTAGE<br>PAID<br>EDDM RETAIL</div>
  <div class="mail-to">Local<br>Postal Customer</div>

  <div class="portrait" role="img" aria-label="Portrait of Laura Bellamy"></div>

  <div class="cover-id">Laura Bellamy<br>Realtor ®<small>DRE# 02281745</small></div>
  <p class="cover-message">Please feel welcome to call on me<br>for all things home-related.<br>I will look forward to meeting you!</p>

  <div class="partner">
    <span class="partner-circle"></span>
    <span class="partner-name">Summit Realty</span>
  </div>

  <h3 class="footer-name footer-name--left">LAURA BELLAMY</h3>
  <ul class="contact-list contact-list--left">
    <li><svg viewBox="0 0 10 10"><circle cx="5" cy="5" r="4.4" fill="none" stroke="#fff" stroke-width=".8"/><path d="M3.3 2.8l1 1-.5.6a4 4 0 0 0 1.8 1.8l.6-.5 1 1-.7.8C4.6 7.2 2.8 5.4 2.5 3.5z" fill="#fff"/></svg>555 014 2283</li>
    <li><svg viewBox="0 0 10 10"><circle cx="5" cy="5" r="4.4" fill="none" stroke="#fff" stroke-width=".8"/><rect x="2.6" y="3.3" width="4.8" height="3.4" fill="none" stroke="#fff" stroke-width=".7"/><path d="M2.6 3.3L5 5.2l2.4-1.9" fill="none" stroke="#fff" stroke-width=".7"/></svg>laura@bellamyhomes.com</li>
    <li><svg viewBox="0 0 10 10"><circle cx="5" cy="5" r="4.4" fill="none" stroke="#fff" stroke-width=".8"/><circle cx="5" cy="5" r="2.6" fill="none" stroke="#fff" stroke-width=".6"/><path d="M2.4 5h5.2M5 2.4v5.2" stroke="#fff" stroke-width=".6"/></svg>www.bellamyhomes.com</li>
  </ul>

  <span class="badge badge--one" aria-hidden="true"></span>
  <span class="badge badge--two" aria-hidden="true"></span>
</section>

</body>
</html>
```